QTR Business Card

Harborline Capital Partners is a successful and reputable financial services company.Our main services are home loans, commercial loans, vehicle finance and equipment finance. We also do development finance for property developers. Our company is always evolving to always be an industry leader in best financial service practices with access to the largest range of lenders in the country.

We want the business card to reflect our national finance company. Modern, professional corporate image. At the same time the concept of Harborline Capital Partners is that we help build wealth for you but the process for the client is an enjoyable peaceful experience. Not stressful at all .....

Colors to be same as the logo .... gold silver black white as the options

On the reverse side of the card I wanted either just the logo symbol or the logo symbol and text of the logo ....

It could be on a black background ..... or silver or gold .... want it to be quite striking to look at when you first see the card.

On the other side of the card I wanted the following details:

Doran Pelham
Director

0498 372 604

doran@hbcpx.com.au

Po Box 852
Tarrow ACT 2694

www.hbcpx.com.au

ACN 918 264 057 (This can be in very small print and can be in the bottom corner of the card or somewhere not very prominent)
Updates

As requested Ive uploaded the logo file in both .ai and .pdf formats. Please let me know if you need anything else. Thanks

Reason: Still deciding on which design I like best. I will provide individual feedback as well.

```html
<!DOCTYPE html>
<html lang="en">
<head>
<meta charset="utf-8">
<title>QTR Business Card</title>
<link rel="stylesheet" href="https://fonts.googleapis.com/css2?family=Source+Sans+3:wght@400;600;700&display=swap">
<style>
  :root {
    --page: #eeeeee;
    --card: #fbfbfb;
    --gold: #c9a227;
    --gold-deep: #b28a1a;
    --silver: #9a9a9a;
    --ink: #3a3a3a;
    --muted: #555555;
  }
  * { box-sizing: border-box; margin: 0; padding: 0; }
  html, body {
    width: 1200px; height: 720px; overflow: hidden;
    background: var(--page);
    font-family: "Source Sans 3", "Helvetica Neue", Arial, sans-serif;
  }
  .canvas {
    position: relative; width: 1200px; height: 720px;
    display: flex; align-items: center; justify-content: center; gap: 60px;
  }
  .card {
    position: relative;
    width: 525px; height: 300px;
    background: var(--card);
    border-radius: 4px;
    box-shadow: 0 2px 6px rgba(0,0,0,0.08), 0 12px 30px rgba(0,0,0,0.06);
  }
  .brand { display: flex; align-items: center; gap: 14px; }
  .brand-mark {
    width: 58px; height: 58px; border-radius: 50%;
    border: 4px solid var(--silver);
    background: #ffffff;
    flex: none;
  }
  .brand-name {
    color: var(--gold);
    font-weight: 600;
    font-size: 23px;
    letter-spacing: 1.5px;
    text-transform: uppercase;
    line-height: 1;
  }
  .card-front { display: flex; align-items: center; justify-content: center; }
  .card-front .brand-mark { width: 70px; height: 70px; }
  .card-front .brand-name { font-size: 25px; }

  .card-back { padding: 34px 40px; }
  .card-back .brand-mark { width: 52px; height: 52px; }
  .card-back .brand-name { font-size: 20px; }
  .details { margin-left: 66px; margin-top: 18px; }
  .person-name { color: var(--gold); font-weight: 700; font-size: 18px; line-height: 1.1; }
  .person-role { color: var(--ink); font-size: 13px; margin-bottom: 12px; }
  .contact { list-style: none; margin-bottom: 10px; }
  .contact li {
    display: flex; align-items: center; gap: 7px;
    color: var(--ink); font-size: 13px; line-height: 1.45;
  }
  .contact svg { width: 11px; height: 11px; fill: var(--gold); flex: none; }
  .address { color: var(--gold-deep); font-weight: 700; font-size: 12.5px; line-height: 1.15; margin-bottom: 12px; }
  .company-number { color: var(--muted); font-size: 12px; letter-spacing: 0.5px; }
</style>
</head>
<body>
<main class="canvas">
  <section class="card card-front" aria-label="Card front">
    <div class="brand">
      <span class="brand-mark"></span>
      <span class="brand-name">Harborline Capital Partners</span>
    </div>
  </section>

  <section class="card card-back" aria-label="Card back">
    <div class="brand">
      <span class="brand-mark"></span>
      <span class="brand-name">Harborline Capital Partners</span>
    </div>
    <div class="details">
      <p class="person-name">Doran Pelham</p>
      <p class="person-role">Director</p>
      <ul class="contact">
        <li>
          <svg viewBox="0 0 24 24" aria-hidden="true"><path d="M6.6 10.8a15.1 15.1 0 0 0 6.6 6.6l2.2-2.2c.3-.3.7-.4 1-.2 1.1.4 2.3.6 3.6.6.6 0 1 .4 1 1V20c0 .6-.4 1-1 1A17 17 0 0 1 3 4c0-.6.4-1 1-1h3.5c.6 0 1 .4 1 1 0 1.3.2 2.5.6 3.6.1.3 0 .7-.2 1z"/></svg>
          0498 372 604
        </li>
        <li>
          <svg viewBox="0 0 24 24" aria-hidden="true"><path d="M2 5h20v14H2z M3.5 6.5 12 13l8.5-6.5" fill="var(--gold)"/><path d="M3.5 7 12 13.2 20.5 7" fill="none" stroke="#fff" stroke-width="1.6"/></svg>
          doran@hbcpx.com.au
        </li>
        <li>
          <svg viewBox="0 0 24 24" aria-hidden="true"><circle cx="12" cy="12" r="10"/><path d="M2 12h20M12 2c3 3 3 17 0 20M12 2c-3 3-3 17 0 20" fill="none" stroke="#fff" stroke-width="1.4"/></svg>
          www.hbcpx.com.au
        </li>
      </ul>
      <p class="address">Po Box 852<br>Tarrow ACT 2694</p>
      <p class="company-number">ACN 918 264 057</p>
    </div>
  </section>
</main>
</body>
</html>
```